Spa Business Card Design Project

Hello! We are a boutique spa for men and women that is rebranding. I would like a memorable new business card that showcases our beautiful new logo and our unique business. I would like it to be classic/timeless and eclectic/artistic at the  same time.
I am a fan of negative space as you can tell from the logo. I am also open to any creative ideas.
Multi sided design. Two sided design is acceptable as an option, too. "Flaps/folds/whatever the design term is" are optional- whether full vertical or horizontal, half flap, full flap etc
On either side next to the golden snail I would potentially like to see "slow down. Enjoy Life."  Possibly on one statment on top of each other, crowned with the snail. Or the statment following the snail on one line... I am open for a creative suprise, too.
The back I would like room for the standard Information
"3817 Birch Lane
Ashbrook, Vermont 05734
(518) 462 3085
info@thecorvella spa.com
The snail is to be done in gold ink.
Can I also Have an option for cards that are individualized for staff members, too?

Updates
Project Deadline Extended
Reason: I apologize for the deadline extension. My day was more involved than anticipated in other matters. Hope to have this closed by next Tuesday.
Thank you

Target Market(s)
Men and women with expendable income between the ages of 30-55
Industry/Entity Type
Boutique
Requirements
Must have
- only black and gold ink.

Nice to have
- One of a kind.
Showcase the snail :-)
make you smile :-)
Fun, but professional.
Should not have
- Lots of color.
Too feminine.
Too busy.

```html
<!DOCTYPE html>
<html lang="en">
<head>
<meta charset="utf-8">
<title>The Corvella Spa – Business Cards</title>
<link href="https://fonts.googleapis.com/css2?family=Didact+Gothic&family=Montserrat:wght@700&display=swap" rel="stylesheet">
<style>
  :root {
    --backdrop: #2a2a2a;
    --card-black: #080808;
    --card-white: #f7f7f5;
    --gold: #b8974e;
    --ink: #1a1a1a;
    --faint-gold: #efe8d8;
  }
  * { box-sizing: border-box; margin: 0; padding: 0; }
  html, body { width: 1200px; height: 900px; overflow: hidden; }
  body {
    background: var(--backdrop);
    font-family: "Didact Gothic", "Century Gothic", sans-serif;
    position: relative;
  }
  .card {
    position: absolute;
    left: 320px;
    width: 560px;
    height: 320px;
    box-shadow: 0 10px 30px rgba(0,0,0,.5);
    overflow: hidden;
  }
  .card-front { top: 60px; background: var(--card-black); }
  .card-back { top: 430px; background: var(--card-white); }

  .front-brand {
    position: absolute; inset: 0;
    display: flex; flex-direction: column; align-items: center; justify-content: center;
    color: var(--gold);
  }
  .front-brand .brand-name { font-size: 44px; letter-spacing: 2px; white-space: nowrap; }
  .front-brand .tagline { font-size: 17px; margin-top: 6px; }
  .front-brand .web { font-size: 13px; margin-top: 22px; letter-spacing: .5px; }

  .back-decor { position: absolute; left: 250px; top: -30px; width: 380px; height: 380px; }

  .back-brand {
    position: absolute; left: 28px; top: 120px; width: 212px;
    text-align: center; color: var(--ink);
  }
  .back-brand .brand-name { font-size: 24px; letter-spacing: .5px; white-space: nowrap; }
  .back-brand .tagline { font-size: 10.5px; margin-top: 4px; white-space: nowrap; }

  .divider {
    position: absolute; left: 248px; top: 90px; width: 1px; height: 84px; background: var(--ink);
  }
  .contact {
    position: absolute; left: 262px; top: 94px;
    font-size: 12.5px; line-height: 1.3; color: var(--ink);
    white-space: nowrap;
  }
  .contact .gap { height: 10px; }
  .contact .label { color: var(--gold); font-weight: bold; margin-right: 3px; }

  .mark-dot {
    position: absolute; left: 466px; top: 136px;
    width: 34px; height: 34px; border-radius: 50%; background: var(--gold);
  }
  .motto {
    position: absolute; right: 40px; top: 228px;
    font-size: 19px; color: var(--ink); white-space: nowrap;
  }
  .motto strong { font-family: "Montserrat", sans-serif; font-weight: 700; font-size: 16px; }
</style>
</head>
<body>
  <section class="card card-front">
    <div class="front-brand">
      <div class="brand-name">The Corvella Spa</div>
      <div class="tagline">a boutique spa for Men &amp; Women</div>
      <div class="web">www.TheCorvellaSpa.com</div>
    </div>
  </section>

  <section class="card card-back">
    <svg class="back-decor" viewBox="0 0 380 380" role="img" aria-label="Large faint gold brand emblem in the background">
      <circle cx="190" cy="190" r="180" fill="var(--faint-gold)"/>
    </svg>

    <div class="back-brand">
      <div class="brand-name">The Corvella Spa</div>
      <div class="tagline">a boutique spa for Men &amp; Women</div>
    </div>

    <div class="divider"></div>

    <div class="contact">
      <div>3817 Birch Lane</div>
      <div>Ashbrook, Vermont 05734</div>
      <div class="gap"></div>
      <div><span class="label">P</span>(518) 462 3085</div>
      <div><span class="label">E</span>info@thecorvellaspa.com</div>
    </div>

    <div class="mark-dot"></div>

    <div class="motto">slow down......... <strong>Enjoy Life</strong></div>
  </section>
</body>
</html>
```